Quorbix new startup tech website refresh

We need a new website design for a tech startup company. We want a cutting edge high tech looking website. See quorbix-example.com for the current site that needs to be updated with a fresh look. Use the info from the website.
We want the site to feel fast, sleek, and tech-driven while still speaking directly to the customers who will use Quorbix. The design should highlight speed, efficiency, and precision with a monospace code font for headlines, stats, and technical details, paired with a clean sans-serif for body copy. This reinforces the product’s engineering credibility while keeping content easy to read.

Target Market(s)

tech Enterprises, Start up companies and Cloud providers

Industry/Entity Type

Tech

Number of Pages Required

2 page

Requirements
Must have
• We want the site to feel fast, sleek, and tech-driven while still speaking directly to the customers who will use Quorbix. The design should highlight speed, efficiency, and precision with a monospace code font for headlines, stats, and technical details, paired with a clean sans-serif for body copy. This reinforces the product’s engineering credibility while keeping content easy to read.

```html
<!DOCTYPE html>
<html lang="en">
<head>
<meta charset="utf-8">
<title>Quorbix — Precision-Engineered Solutions</title>
<link href="https://fonts.googleapis.com/css2?family=JetBrains+Mono:wght@400;700;800&family=Lato:ital,wght@0,300;0,400;1,300&display=swap" rel="stylesheet">
<style>
:root{
  --bg:#0f1629;
  --card:#1c2639;
  --band:#1e212b;
  --accent:#4f46e5;
  --accent-soft:#5b53f0;
  --text:#e8ebf2;
  --muted:#b4bccb;
  --dim:#8d96a8;
  --line:#1d2538;
}
*{box-sizing:border-box;margin:0;padding:0}
html,body{width:1200px;height:3480px;overflow:hidden}
body{background:var(--bg);color:var(--text);font-family:"Lato",sans-serif;position:relative}
.mono{font-family:"JetBrains Mono",monospace}
.abs{position:absolute}
.site-header{position:absolute;top:0;left:100px;width:1000px;height:90px}
.brand{position:absolute;left:0;top:31px;font:700 23px "JetBrains Mono",monospace;color:var(--text)}
.nav{position:absolute;right:0;top:20px;display:flex;align-items:center;gap:0}
.nav a{font:400 12px "JetBrains Mono",monospace;color:var(--dim);text-decoration:none;margin-left:40px}
.nav .nav-cta{background:var(--accent);color:#9aa0e8;padding:14px 14px 2px;height:30px;border-radius:3px;margin-left:40px}
.hero{position:absolute;top:145px;left:0;width:1200px;text-align:center}
.hero h1{font:700 51px/64px "JetBrains Mono",monospace;color:var(--text);width:920px;margin:0 auto}
.hero h1 span{color:var(--accent)}
.hero p{margin-top:26px;font-size:13.5px;color:var(--muted)}
.hero-actions{margin-top:15px;display:flex;justify-content:center;gap:5px}
.btn{display:inline-flex;align-items:center;justify-content:center;height:49px;border-radius:25px;font:700 12px "JetBrains Mono",monospace;text-decoration:none;text-transform:uppercase;padding-top:10px}
.btn-primary{background:var(--accent);color:#fff;width:200px;box-shadow:0 6px 22px rgba(79,70,229,.45)}
.btn-outline{border:2px solid var(--accent);color:var(--accent-soft);width:143px}
.section-title{position:absolute;left:0;width:1200px;text-align:center;font:700 40px/48px "JetBrains Mono",monospace;color:var(--text)}
.card{position:absolute;width:298px;background:var(--card);border-radius:4px;padding:0 27px}
.card h3{font:700 28px/36px "JetBrains Mono",monospace;color:var(--accent)}
.card p{font-size:13.5px;line-height:21px;color:var(--muted)}
.benefit{height:272px}
.benefit h3{margin-top:40px}
.benefit p{margin-top:34px}
.tenet{height:613px;padding-top:27px}
.tenet .photo{width:244px;height:182px}
.tenet h3{margin-top:36px}
.tenet p{margin-top:36px}
.stat{position:absolute;left:27px;font:400 12px "JetBrains Mono",monospace;color:var(--muted)}
.stat b{font-weight:400;color:var(--accent-soft)}
.faq-item{position:absolute;left:267px;width:665px;height:62px;border:1px solid var(--line);border-radius:3px;display:flex;align-items:center;justify-content:space-between;padding:6px 27px 0}
.faq-item span{font:700 12px "JetBrains Mono",monospace;color:var(--text)}
.faq-item i{font-style:normal;color:var(--accent-soft);font-size:18px;margin-top:-16px}
.testimonials{position:absolute;top:2629px;left:100px;width:1000px;height:486px;background:var(--band)}
.quote{position:absolute;top:128px;width:296px;height:303px;background:var(--bg);border-radius:4px;padding:26px 27px}
.quote .mark{font:italic 300 28px/20px "Lato",sans-serif;color:#3b3a8f;height:18px}
.quote p{font:italic 300 13.5px/25px "Lato",sans-serif;color:var(--muted)}
.quote .who{margin-top:19px;font:700 12px "JetBrains Mono",monospace;color:var(--text)}
.quote .role{margin-top:12px;font:400 11px "JetBrains Mono",monospace;color:var(--muted)}
.cta{position:absolute;top:3186px;left:0;width:1200px;text-align:center}
.cta h2{font:700 40px/48px "JetBrains Mono",monospace}
.cta p{margin-top:14px;font-size:13.5px;color:var(--muted)}
.cta .btn{width:235px;margin-top:14px}
.site-footer{position:absolute;top:3418px;left:100px;width:1000px;font-size:12px;color:var(--muted)}
.site-footer .links{position:absolute;right:0;top:10px;display:flex;gap:20px}
.site-footer a{color:var(--muted);text-decoration:none}
</style>
</head>
<body>
<header class="site-header">
  <div class="brand">Quorbix</div>
  <nav class="nav">
    <a href="#">Home</a>
    <a href="#">Services</a>
    <a href="#" class="nav-cta">Contact Us</a>
  </nav>
</header>

<section class="hero">
  <h1><span>Quorbix</span>: Precision-Engineered Solutions for a Future-Forward World.</h1>
  <p>Unleash unparalleled speed, surgical efficiency, and unwavering precision in your data strategies.</p>
  <div class="hero-actions">
    <a href="#" class="btn btn-primary">Explore Our Services</a>
    <a href="#" class="btn btn-outline">Get in Touch</a>
  </div>
</section>

<h2 class="section-title" style="top:572px">Key Benefits of Partnering with Quorbix</h2>
<article class="card benefit" style="left:113px;top:628px"><h3>Accelerated Insights</h3><p>Transform raw data into actionable intelligence at unprecedented speeds, enabling faster, more informed decision-making.</p></article>
<article class="card benefit" style="left:451px;top:628px"><h3>Optimized Operations</h3><p>Streamline your workflows and reduce operational costs with our surgically efficient data processing and AI automation.</p></article>
<article class="card benefit" style="left:789px;top:628px"><h3>Unrivaled Data Accuracy</h3><p>Gain absolute confidence in your data with our rigorous validation processes, ensuring nearly flawless precision for critical analysis.</p></article>
<article class="card benefit" style="left:113px;top:940px"><h3>Future-Proof Scalability</h3><p>Our cloud-native solutions are built to scale with your business, adapting seamlessly to growing data volumes and evolving technological landscapes.</p></article>
<article class="card benefit" style="left:451px;top:940px"><h3>Enhanced Security</h3><p>Protect your valuable assets with robust, multi-layered cybersecurity protocols integrated into every data solution we provide.</p></article>
<article class="card benefit" style="left:789px;top:940px"><h3>Strategic AI Integration</h3><p>Leverage cutting-edge artificial intelligence to unlock new opportunities, automate complex tasks, and drive innovation across your enterprise.</p></article>

<h2 class="section-title" style="top:1338px;padding:0 200px">Our Core Tenets: Speed, Efficiency, Precision.</h2>
<article class="card tenet" style="left:113px;top:1442px">
  <div class="photo" role="img" aria-label="Skyscraper spire rising into a cloudy blue sky" style="background:linear-gradient(180deg,#5d6f93 0%,#a9b7cf 55%,#7d8aa3 100%)"></div>
  <h3>Speed: Unrivaled Data Velocity</h3>
  <p>Experience data processing at breakthrough speeds. Our architecture is engineered to minimize latency and maximize throughput, ensuring your insights are always real-time and actionable.</p>
  <div class="stat" style="top:563px">Avg. Latency: <b>3ms</b></div>
</article>
<article class="card tenet" style="left:451px;top:1442px">
  <div class="photo" role="img" aria-label="Quiet interior hall with rows of wooden benches in soft light" style="background:linear-gradient(180deg,#3a3a3a 0%,#6a6a6a 50%,#2b2b2b 100%)"></div>
  <h3>Efficiency: Streamlined Operations</h3>
  <p>Optimize resource utilization and reduce operational overhead. Quorbix's solutions are designed for seamless integration and automation, delivering more with less, consistently.</p>
  <div class="stat" style="top:542px">Resource Optimization: <b>98%</b></div>
</article>
<article class="card tenet" style="left:789px;top:1442px">
  <div class="photo" role="img" aria-label="Rocky mountain peak wrapped in white mist" style="background:linear-gradient(100deg,#dcdedd 0%,#c4c6c4 55%,#8a857b 100%)"></div>
  <h3>Precision: Flawless Data Accuracy</h3>
  <p>Trust in the accuracy of your data. Our advanced algorithms and robust validation processes guarantee flawless data integrity, providing the foundation for critical decision-making.</p>
  <div class="stat" style="top:542px">Data Accuracy: <b>99.99%</b></div>
</article>

<h2 class="section-title" style="top:2181px">Frequently Asked Questions</h2>
<div class="faq-item" style="top:2266px"><span>What is Quorbix?</span><i>+</i></div>
<div class="faq-item" style="top:2348px"><span>What types of services does Quorbix offer?</span><i>+</i></div>
<div class="faq-item" style="top:2431px"><span>How does Quorbix ensure data accuracy and precision?</span><i>+</i></div>
<div class="faq-item" style="top:2513px"><span>What sets Quorbix apart from other technology providers?</span><i>+</i></div>

<section class="testimonials">
  <h2 class="section-title" style="left:-100px;top:72px">What Our Clients Say</h2>
  <blockquote class="quote" style="left:13px"><div class="mark">“</div><p>"Quorbix transformed our data operations. The speed and precision they delivered were beyond our expectations, leading to immediate improvements in our decision-making process."</p><div class="who">Mara Lindqvist</div><div class="role">CTO, Northwind Systems</div></blockquote>
  <blockquote class="quote" style="left:351px"><div class="mark">“</div><p>"The efficiency gains we've experienced since partnering with Quorbix are monumental. Their AI integration is seamless and has significantly boosted our productivity."</p><div class="who">Tomas Ferreira</div><div class="role">Operations Director, Crestline Freight</div></blockquote>
  <blockquote class="quote" style="left:689px"><div class="mark">“</div><p>"We rely on Quorbix for the most critical data analytics. Their unwavering precision ensures we always have the most accurate insights to drive our strategic growth."</p><div class="who">Nadia Okafor</div><div class="role">CEO, Brightpath Media Co</div></blockquote>
</section>

<section class="cta">
  <h2>Ready to Elevate Your Enterprise?</h2>
  <p>Partner with Quorbix and transform your data into a strategic advantage. Let's build your elevated digital future together.</p>
  <a href="#" class="btn btn-primary">Start Your Transformation</a>
</section>

<footer class="site-footer">
  <div>© 2024 Quorbix. All Rights Reserved.</div>
  <div class="links"><a href="#">Privacy Policy</a><a href="#">Terms of Service</a><a href="#">Sitemap</a></div>
</footer>
</body>
</html>
```